New Business Card Design Project

2 sided business card required. I have attached some previous designs of items we have had made so you can see the logo etc. we Want the card to look professional and modern. for the final design upload for winning designer please note I need to be able to edit the names / phone numbers on the card design as I need to get them made for different staff.
Updates

extending time so designers can have time to submit

Target Market(s)

new customers

Industry/Entity Type

transport / earthmoving

Contact Information for Business Card

name, phone number email address

Requirements
Nice to have
• professional / impressive looking card (first impressions to customers count)
Should not have
• do not put our mobile number on the design use a generic number

```html
<!DOCTYPE html>
<html lang="en">
<head>
<meta charset="utf-8">
<title>KDT Pty Ltd – Business Card</title>
<link rel="stylesheet" href="https://fonts.googleapis.com/css2?family=Russo+One&family=Michroma&family=Lato:wght@400;700;900&display=swap">
<style>
  :root {
    --backdrop: #666666;
    --card-black: #050505;
    --pattern-mid: #2a2b2d;
    --copper: #c98b55;
    --copper-light: #e0a66f;
    --silver: #d3d6da;
    --white: #ffffff;
    --muted: #e6e6e6;
    --earth-dark: #6d3b22;
    --earth: #b0673e;
    --earth-light: #c98758;
  }
  * { box-sizing: border-box; margin: 0; padding: 0; }
  html, body {
    width: 1200px; height: 924px; overflow: hidden;
    background: var(--backdrop);
    font-family: "Lato", sans-serif;
  }
  .card {
    position: absolute; left: 280px;
    width: 640px; height: 366px;
    border-radius: 14px; overflow: hidden;
    background: var(--card-black);
    color: var(--white);
  }
  .card--front { top: 71px; }
  .card--back { top: 487px; }

  .pattern-area {
    position: absolute;
    background: radial-gradient(ellipse at 50% 45%, var(--pattern-mid) 0%, #141516 45%, var(--card-black) 78%);
  }
  .card--front .pattern-area { left: 0; top: 0; width: 640px; height: 230px; }
  .card--back .pattern-area { left: 0; top: 0; width: 360px; height: 165px; }

  .wordmark { position: absolute; font-family: "Russo One", sans-serif; color: var(--silver); line-height: 1; }
  .wordmark__name { position: absolute; white-space: nowrap; }
  .wordmark__suffix { position: absolute; white-space: nowrap; }
  .card--front .wordmark__name { left: 178px; top: 60px; font-size: 96px; letter-spacing: 4px; }
  .card--front .wordmark__suffix { left: 482px; top: 140px; font-size: 24px; }
  .card--back .wordmark__name { left: 66px; top: 42px; font-size: 62px; letter-spacing: 3px; }
  .card--back .wordmark__suffix { left: 263px; top: 94px; font-size: 16px; }

  .fleet-photo {
    position: absolute; left: 0; top: 200px; width: 640px; height: 166px;
    background: linear-gradient(180deg, #1b1b1b 0%, #2e2a27 38%, var(--earth-dark) 55%, var(--earth) 78%, var(--earth-light) 100%);
  }

  .band {
    position: absolute; height: 22px;
    background: var(--copper);
    clip-path: polygon(0 0, 100% 0, calc(100% - 12px) 100%, 0 100%);
    font-family: "Russo One", sans-serif; color: #111;
    font-size: 16px; line-height: 22px;
  }
  .band--company { left: 0; top: 165px; width: 196px; padding-left: 36px; }
  .band--services { left: 357px; top: 18px; width: 165px; padding-left: 8px; font-size: 16px; }

  .person__name {
    position: absolute; left: 35px; top: 198px;
    font-family: "Michroma", sans-serif; font-weight: 400; font-size: 16px; letter-spacing: 0.5px;
  }
  .person__role {
    position: absolute; left: 35px; top: 222px;
    font-family: "Michroma", sans-serif; font-size: 11px; color: var(--copper-light); letter-spacing: 0.5px;
  }
  .contacts { position: absolute; left: 36px; top: 249px; list-style: none; }
  .contacts li {
    display: flex; align-items: flex-start; gap: 9px;
    font-size: 14px; line-height: 18px; margin-bottom: 4px; color: var(--muted);
  }
  .contacts svg { width: 16px; height: 16px; flex: none; margin-top: 1px; }

  .services { position: absolute; left: 357px; top: 50px; width: 260px; list-style: none; }
  .services li {
    display: flex; align-items: flex-start; gap: 8px;
    font-size: 13px; line-height: 16px; margin-bottom: 5.6px; color: var(--muted);
  }
  .services svg { width: 10px; height: 10px; flex: none; margin-top: 3px; }
  .services__note {
    position: absolute; left: 357px; top: 308px; width: 250px;
    font-size: 12px; font-weight: 900; line-height: 16.5px; text-align: justify;
  }
</style>
</head>
<body>

<section class="card card--front" aria-label="Business card front">
  <div class="pattern-area" role="img" aria-label="Dark metallic mesh background"></div>
  <div class="fleet-photo" role="img" aria-label="Photo of a road train hauling side-tipper trailers on a red dirt outback road"></div>
  <div class="wordmark">
    <span class="wordmark__name">KDT</span>
    <span class="wordmark__suffix">Pty Ltd</span>
  </div>
</section>

<section class="card card--back" aria-label="Business card back">
  <div class="pattern-area" role="img" aria-label="Dark metallic mesh background"></div>
  <div class="wordmark">
    <span class="wordmark__name">KDT</span>
    <span class="wordmark__suffix">Pty Ltd</span>
  </div>

  <div class="band band--company">KDT PTY LTD</div>
  <h1 class="person__name">DANIEL CORRIE</h1>
  <p class="person__role">DIRECTOR</p>

  <ul class="contacts">
    <li>
      <svg viewBox="0 0 16 16"><circle cx="8" cy="8" r="8" fill="#d9d9d9"/><path d="M5.2 4.2l1.6-.3.8 2-1 .8a5.5 5.5 0 0 0 2.7 2.7l.8-1 2 .8-.3 1.6c-4 .3-7-2.7-6.6-6.6z" fill="#222"/></svg>
      013 456 7890
    </li>
    <li>
      <svg viewBox="0 0 16 16"><circle cx="8" cy="8" r="8" fill="#d9d9d9"/><rect x="4" y="5" width="8" height="6" rx="1" fill="none" stroke="#222" stroke-width="1.2"/><path d="M4.3 5.4L8 8.3l3.7-2.9" fill="none" stroke="#222" stroke-width="1.2"/></svg>
      accounts@kdthaulage.com.au
    </li>
    <li>
      <svg viewBox="0 0 16 16"><circle cx="8" cy="8" r="8" fill="#d9d9d9"/><g fill="none" stroke="#222" stroke-width="1"><circle cx="8" cy="8" r="4.5"/><ellipse cx="8" cy="8" rx="2" ry="4.5"/><path d="M3.5 8h9M4.2 5.8h7.6M4.2 10.2h7.6"/></g></svg>
      www.kdthaulage.com.au
    </li>
    <li>
      <svg viewBox="0 0 16 16"><circle cx="8" cy="8" r="8" fill="#d9d9d9"/><path d="M8 3.5a3 3 0 0 0-3 3c0 2.2 3 5 3 5s3-2.8 3-5a3 3 0 0 0-3-3z" fill="none" stroke="#222" stroke-width="1.2"/><circle cx="8" cy="6.5" r="1" fill="#222"/><path d="M4.5 12.5h7" stroke="#222" stroke-width="1"/></svg>
      <span>Depot: Lot 45, Ironstone Track Road<br>Red Plains, Australia</span>
    </li>
  </ul>

  <div class="band band--services">OUR SERVICES</div>
  <ul class="services">
    <li><svg viewBox="0 0 10 10"><circle cx="5" cy="5" r="5" fill="#cfcfcf"/><path d="M2.8 5.2l1.5 1.4 3-3" fill="none" stroke="#111" stroke-width="1.3"/></svg>Over size loads / Hot Shot Loads</li>
    <li><svg viewBox="0 0 10 10"><circle cx="5" cy="5" r="5" fill="#cfcfcf"/><path d="M2.8 5.2l1.5 1.4 3-3" fill="none" stroke="#111" stroke-width="1.3"/></svg>Heavy Vehicle Recovery services</li>
    <li><svg viewBox="0 0 10 10"><circle cx="5" cy="5" r="5" fill="#cfcfcf"/><path d="M2.8 5.2l1.5 1.4 3-3" fill="none" stroke="#111" stroke-width="1.3"/></svg>Potable Water Deliveries</li>
    <li><svg viewBox="0 0 10 10"><circle cx="5" cy="5" r="5" fill="#cfcfcf"/><path d="M2.8 5.2l1.5 1.4 3-3" fill="none" stroke="#111" stroke-width="1.3"/></svg>Road Building / Maintenance</li>
    <li><svg viewBox="0 0 10 10"><circle cx="5" cy="5" r="5" fill="#cfcfcf"/><path d="M2.8 5.2l1.5 1.4 3-3" fill="none" stroke="#111" stroke-width="1.3"/></svg>Earthworks</li>
    <li><svg viewBox="0 0 10 10"><circle cx="5" cy="5" r="5" fill="#cfcfcf"/><path d="M2.8 5.2l1.5 1.4 3-3" fill="none" stroke="#111" stroke-width="1.3"/></svg>Sand &amp; Metal Supply &amp; Cartage</li>
    <li><svg viewBox="0 0 10 10"><circle cx="5" cy="5" r="5" fill="#cfcfcf"/><path d="M2.8 5.2l1.5 1.4 3-3" fill="none" stroke="#111" stroke-width="1.3"/></svg>Road Train Tippers</li>
    <li><svg viewBox="0 0 10 10"><circle cx="5" cy="5" r="5" fill="#cfcfcf"/><path d="M2.8 5.2l1.5 1.4 3-3" fill="none" stroke="#111" stroke-width="1.3"/></svg>Road Train Tankers</li>
    <li><svg viewBox="0 0 10 10"><circle cx="5" cy="5" r="5" fill="#cfcfcf"/><path d="M2.8 5.2l1.5 1.4 3-3" fill="none" stroke="#111" stroke-width="1.3"/></svg>Road Train Flat Tops</li>
    <li><svg viewBox="0 0 10 10"><circle cx="5" cy="5" r="5" fill="#cfcfcf"/><path d="M2.8 5.2l1.5 1.4 3-3" fill="none" stroke="#111" stroke-width="1.3"/></svg>Drop Deck Trailers</li>
    <li><svg viewBox="0 0 10 10"><circle cx="5" cy="5" r="5" fill="#cfcfcf"/><path d="M2.8 5.2l1.5 1.4 3-3" fill="none" stroke="#111" stroke-width="1.3"/></svg>Mine site accredited equipment &amp; Operators</li>
  </ul>
  <p class="services__note">We offer a large range of services not listed so call us today for a personalised quote to suit your needs.</p>
</section>

</body>
</html>
```